Organic rose water based skincare line in need of product label and packaging design

We are looking for a simple, clean, modern labeling and packaging design for 2 of our products. Our brand's demographic is upscale females ages 20-40. We want our packaging to be very minimalistic, and instagramable.

Product #1: Rose water facial spray "Lumi Mist"
Product #2: Rose water facial toner "Velvet Hush Hour"

Please see attached images for our current logo and label design. We have also added some images that inspire our branding.

Target Market(s)

trendy woman ages 20-40

Industry/Entity Type

Skin Care Product

Font styles to use
Serif
Sans Serif

Colors

Designer to choose only greyscale colors for use in the design.

Requirements
Must have
• Must have our logo, bottle size, product name on front and how to use and ingredient on the back. Please see project description and attached images for more information.
Should not have
• Too much going on or too many colors.

```html
<!DOCTYPE html>
<html lang="en">
<head>
<meta charset="utf-8">
<title>Petal Atelier – Lumi Mist packaging</title>
<link rel="stylesheet" href="https://fonts.googleapis.com/css2?family=Comfortaa:wght@400&family=Quicksand:wght@400&family=Playfair+Display:ital@1&family=Cormorant+Garamond:wght@400&display=swap">
<style>
  :root {
    --page-bg: #ffffff;
    --box-pink: #f9ecf4;
    --label-white: #f7f6f6;
    --label-edge: #e3e1e1;
    --ink-dark: #3a3839;
    --ink-soft: #6e6a6b;
    --rule: #8a8687;
    --floral-gold: #e9c48f;
    --floral-fade: rgba(233, 196, 143, 0);
  }
  * { margin: 0; padding: 0; box-sizing: border-box; }
  html, body { width: 1200px; height: 942px; overflow: hidden; background: var(--page-bg); }
  .canvas { position: relative; width: 1200px; height: 942px; }

  .panel { position: absolute; text-align: center; color: var(--ink-dark); }
  .box-front { left: 250px; top: 35px; width: 290px; height: 815px; background: var(--box-pink); }
  .bottle-label { left: 660px; top: 410px; width: 250px; height: 420px; background: var(--label-white); border: 1px solid var(--label-edge); border-radius: 10px; }

  .floral-art { position: absolute; border-radius: 40% 45% 35% 50%;
    background: radial-gradient(ellipse at 55% 45%, rgba(233,196,143,0.45), var(--floral-fade) 70%); }
  .box-front .floral-art { left: 30px; top: 225px; width: 250px; height: 540px; }
  .bottle-label .floral-art { left: 45px; top: 110px; width: 150px; height: 260px; }

  .brand-name { position: absolute; font-family: "Quicksand", sans-serif; font-weight: 400; text-align: left; line-height: 0.95; color: var(--ink-dark); }
  .box-front .brand-name { left: 35px; top: 92px; font-size: 30px; }
  .bottle-label .brand-name { left: 112px; top: 20px; font-size: 17px; }

  .product-name { position: absolute; left: 0; width: 100%; font-family: "Comfortaa", sans-serif; font-weight: 400; letter-spacing: -1px; line-height: 1; }
  .box-front .product-name { top: 462px; font-size: 96px; }
  .bottle-label .product-name { top: 178px; font-size: 60px; }

  .product-sub { position: absolute; left: 0; width: 100%; font-family: "Comfortaa", sans-serif; line-height: 1; }
  .box-front .product-sub { top: 564px; font-size: 32px; }
  .bottle-label .product-sub { top: 244px; font-size: 21px; }

  .descriptor { position: absolute; left: 0; width: 100%; font-family: "Playfair Display", serif; font-style: italic; color: var(--ink-soft); }
  .box-front .descriptor { top: 650px; font-size: 19px; }
  .bottle-label .descriptor { top: 286px; font-size: 16px; }

  .claims { position: absolute; left: 50%; transform: translateX(-50%); border-top: 1px solid var(--rule); border-bottom: 1px solid var(--rule);
    font-family: "Cormorant Garamond", serif; color: var(--ink-soft); line-height: 1.5; }
  .box-front .claims { top: 683px; width: 180px; padding: 4px 0 6px; font-size: 16px; }
  .bottle-label .claims { top: 318px; width: 160px; padding: 3px 0 4px; font-size: 14px; }

  .volume { position: absolute; left: 0; width: 100%; font-family: "Cormorant Garamond", serif; color: var(--ink-soft); letter-spacing: 1px; }
  .box-front .volume { top: 768px; font-size: 15px; }
  .bottle-label .volume { top: 385px; font-size: 14px; }
</style>
</head>
<body>
<main class="canvas">
  <section class="panel box-front">
    <div class="floral-art" role="img" aria-label="Gold line illustration of climbing roses and leaves"></div>
    <div class="brand-name">the<br>petal<br>atelier</div>
    <h1 class="product-name">lumi</h1>
    <div class="product-sub">— mist —</div>
    <p class="descriptor">rose water facial spray</p>
    <div class="claims">organic rosewater<br>hydrating mist</div>
    <div class="volume">2oZ / 60ml</div>
  </section>

  <section class="panel bottle-label">
    <div class="floral-art" role="img" aria-label="Gold line illustration of roses"></div>
    <div class="brand-name">the<br>petal<br>atelier</div>
    <h2 class="product-name">lumi</h2>
    <div class="product-sub">— mist —</div>
    <p class="descriptor">rose water facial spray</p>
    <div class="claims">organic rosewater<br>hydrating mist</div>
    <div class="volume">2oZ / 60ml</div>
  </section>
</main>
</body>
</html>
```